TOVR Enterprise
company business card and envolpe design
TOVR Enterprise -
Creative Brief
Professional
Neeraj Pillai
Director
114, 2c, 2nd floor, Rukminibai Market, Rukminibai Bldg No. 6, Pepper Orchard Lane, Mumbai - 400017.
pillaineeraj41@postvela.example
Should look same as the logo. Business card and Stationery should also be very professional.
TOVR Enterprise is the parent company underwhich many other firms are going to start. So back of the card should be designed in way that i can add the name of other firms.

```html
<!DOCTYPE html>
<html lang="en">
<head>
<meta charset="utf-8">
<title>TOVR Enterprise – Stationery</title>
<link href="https://fonts.googleapis.com/css2?family=Open+Sans:wght@400;600;700;800&display=swap" rel="stylesheet">
<style>
  :root {
    --bg: #ebebeb;
    --paper: #ffffff;
    --brand-red: #a8232a;
    --ink: #333333;
    --ink-soft: #777777;
    --mark-faint: #e4e4e4;
    --shadow: rgba(0,0,0,0.18);
  }
  * { box-sizing: border-box; margin: 0; padding: 0; }
  html, body { width: 1200px; height: 612px; overflow: hidden; }
  body { background: var(--bg); font-family: "Open Sans", Arial, sans-serif; color: var(--ink); position: relative; }

  .sheet { position: absolute; background: var(--paper); box-shadow: 0 3px 6px var(--shadow); overflow: hidden; }

  .brand { display: flex; align-items: center; gap: 4px; }
  .brand__dot { border-radius: 50%; background: var(--brand-red); flex: none; }
  .brand__name { color: var(--brand-red); font-weight: 800; line-height: 1; letter-spacing: 0.5px; }

  .faint-mark { position: absolute; border-radius: 50%; background: var(--mark-faint); }

  /* business cards */
  .card { height: 88px; }
  .card--front .brand { position: absolute; left: 10px; top: 12px; }
  .card .brand__dot { width: 22px; height: 22px; }
  .card .brand__name { font-size: 24px; }
  .card__person { position: absolute; left: 14px; top: 48px; }
  .card__name { font-size: 8px; font-weight: 700; }
  .card__role { font-size: 6px; color: var(--ink-soft); }
  .card--back .card__person { left: 10px; top: 12px; }
  .contact { position: absolute; font-size: 5px; line-height: 8px; color: var(--ink); }
  .contact li { list-style: none; display: flex; align-items: center; gap: 3px; }
  .contact li::before { content: ""; width: 4px; height: 4px; border-radius: 50%; background: var(--brand-red); }

  /* compliment slip */
  .slip .brand { position: absolute; left: 14px; top: 16px; }
  .slip .brand__dot { width: 26px; height: 26px; }
  .slip .brand__name { font-size: 28px; }
  .slip__person { position: absolute; left: 200px; top: 14px; font-size: 9px; font-weight: 700; }
  .slip__person span { font-size: 6px; font-weight: 400; color: var(--ink-soft); }

  /* letterheads */
  .letterhead .brand { position: absolute; left: 16px; top: 18px; }
  .letterhead .brand__dot { width: 24px; height: 24px; }
  .letterhead .brand__name { font-size: 26px; }
  .address-block { position: absolute; right: 16px; top: 18px; width: 175px; font-size: 5px; line-height: 7px; color: var(--ink); display: flex; gap: 10px; }
  .address-block p { width: 90px; }
  .letterhead__footer { position: absolute; left: 0; right: 0; bottom: 12px; text-align: center; font-size: 5px; color: var(--ink); }
  .letterhead__footer::before { content: ""; display: block; height: 1px; background: var(--brand-red); margin: 0 16px 4px; }
</style>
</head>
<body>

  <!-- business cards, left pair -->
  <section class="sheet card card--front" style="left:24px;top:29px;width:190px;">
    <div class="faint-mark" style="right:-20px;top:-18px;width:90px;height:90px;"></div>
    <div class="brand"><span class="brand__dot"></span><span class="brand__name">TOVR</span></div>
    <div class="card__person"><p class="card__name">Neeraj Pillai</p><p class="card__role">Director</p></div>
  </section>
  <section class="sheet card card--back" style="left:228px;top:29px;width:180px;">
    <div class="faint-mark" style="right:-20px;top:-18px;width:90px;height:90px;"></div>
    <div class="card__person"><p class="card__name">Neeraj Pillai</p><p class="card__role">Director</p></div>
    <ul class="contact" style="left:10px;top:44px;">
      <li>+91 22 4000 1234</li>
      <li>+91 98000 11223</li>
      <li>pillaineeraj41@postvela.example</li>
      <li>Pepper Orchard Lane, Mumbai</li>
    </ul>
  </section>

  <!-- business cards, right pair -->
  <section class="sheet card card--front" style="left:463px;top:29px;width:142px;">
    <div class="faint-mark" style="right:-20px;top:-18px;width:80px;height:80px;"></div>
    <div class="brand"><span class="brand__dot"></span><span class="brand__name">TOVR</span></div>
    <div class="card__person"><p class="card__name">Neeraj Pillai</p><p class="card__role">Director</p></div>
  </section>
  <section class="sheet card card--back" style="left:619px;top:29px;width:173px;">
    <div class="faint-mark" style="right:-20px;top:-18px;width:80px;height:80px;"></div>
    <div class="card__person"><p class="card__name">Neeraj Pillai</p><p class="card__role">Director</p></div>
    <ul class="contact" style="left:10px;top:44px;">
      <li>+91 22 4000 1234</li>
      <li>+91 98000 11223</li>
      <li>pillaineeraj41@postvela.example</li>
      <li>Pepper Orchard Lane, Mumbai</li>
    </ul>
  </section>

  <!-- compliment slip -->
  <section class="sheet slip" style="left:29px;top:144px;width:422px;height:144px;">
    <div class="faint-mark" style="right:-10px;top:-30px;width:170px;height:170px;"></div>
    <div class="brand"><span class="brand__dot"></span><span class="brand__name">TOVR</span></div>
    <p class="slip__person" style="left:auto;right:110px;">Neeraj Pillai <span>Director</span></p>
    <ul class="contact" style="left:auto;right:110px;top:30px;">
      <li>+91 22 4000 1234</li>
      <li>pillaineeraj41@postvela.example</li>
    </ul>
  </section>

  <!-- envelope -->
  <section class="sheet envelope" style="left:29px;top:307px;width:422px;height:257px;">
    <svg width="422" height="257" viewBox="0 0 422 257" aria-hidden="true">
      <defs>
        <linearGradient id="flap" x1="0" y1="0" x2="0" y2="1">
          <stop offset="0" stop-color="#f2f2f2"/>
          <stop offset="1" stop-color="#dcdcdc"/>
        </linearGradient>
      </defs>
      <polygon points="0,0 422,0 211,120" fill="url(#flap)"/>
      <polyline points="0,257 175,118" fill="none" stroke="#e2e2e2" stroke-width="1"/>
      <polyline points="422,257 247,118" fill="none" stroke="#e2e2e2" stroke-width="1"/>
      <circle cx="211" cy="98" r="24" fill="#ffffff" stroke="#d6d6d6"/>
    </svg>
  </section>

  <!-- letterhead with footer -->
  <section class="sheet letterhead" style="left:461px;top:137px;width:326px;height:410px;">
    <div class="faint-mark" style="left:83px;top:125px;width:160px;height:160px;"></div>
    <div class="brand"><span class="brand__dot"></span><span class="brand__name">TOVR</span></div>
    <div class="address-block">
      <p>114, 2c, 2nd floor, Rukminibai Market, Rukminibai Bldg No. 6, Pepper Orchard Lane, Mumbai - 400017.</p>
      <p>+91 22 4000 1234<br>+91 98000 11223<br>pillaineeraj41@postvela.example</p>
    </div>
    <p class="letterhead__footer">114, 2c, 2nd floor, Rukminibai Market, Rukminibai Bldg No. 6, Pepper Orchard Lane, Mumbai - 400017.</p>
  </section>

  <!-- letterhead -->
  <section class="sheet letterhead" style="left:804px;top:137px;width:324px;height:410px;">
    <div class="faint-mark" style="left:82px;top:125px;width:160px;height:160px;"></div>
    <div class="brand"><span class="brand__dot"></span><span class="brand__name">TOVR</span></div>
    <div class="address-block">
      <p>114, 2c, 2nd floor, Rukminibai Market, Rukminibai Bldg No. 6, Pepper Orchard Lane, Mumbai - 400017.</p>
      <p>+91 22 4000 1234<br>+91 98000 11223<br>www.tovr.example</p>
    </div>
  </section>

</body>
</html>
```